Zielgruppe
Zielgruppe: M/W, 25-40 J., Unternehmer
Aufgabenstellung
Der Umfang für dieses Projekt besteht aus 3 Bannern in einem Style.
Banner 1: Online-Lösungen
Banner 2: Online-Services
Banner 3: Online-Marketing

```html
<!DOCTYPE html>
<html lang="de">
<head>
<meta charset="utf-8">
<title>Netzhafen – für Ihr Online-Business</title>
<link rel="stylesheet" href="https://fonts.googleapis.com/css2?family=Arimo:wght@400;700&family=Open+Sans:wght@400&display=swap">
<style>
  :root {
    --page-bg: #ebebe9;
    --panel: #ffffff;
    --nav-dark: #3b3b3b;
    --nav-line: #555555;
    --accent-blue: #1e9ad6;
    --active-blue: #2aa8e0;
    --brand-blue: #1b3f7a;
    --text: #444444;
    --heading-grey: #555555;
    --box-grey: #ebebea;
    --banner-frame: #9a9a9a;
    --banner-strip: #3d3d3d;
    --banner-green: #55c400;
    --promo-orange: #f26a1b;
    --btn-red: #e8231d;
    --footer: #444444;
  }
  * { box-sizing: border-box; margin: 0; padding: 0; }
  html, body { width: 1200px; height: 1165px; overflow: hidden; }
  body {
    position: relative;
    background: var(--page-bg);
    font-family: "Arimo", Arial, sans-serif;
    color: var(--text);
  }
  a { color: var(--accent-blue); }

  .site-header {
    position: absolute; left: 0; top: 0; width: 1200px; height: 113px;
    background: linear-gradient(#ffffff 60%, #f1f1f1);
  }
  .brand {
    position: absolute; left: 50px; top: 18px;
    font-family: "Arimo", Arial, sans-serif;
    font-size: 26px; font-weight: 400; color: var(--brand-blue); line-height: 30px;
  }
  .meta-links { position: absolute; left: 366px; top: 26px; display: flex; gap: 18px; font-size: 15.5px; }

  .main-nav {
    position: absolute; left: 50px; top: 75px; width: 1093px; height: 37px;
    background: var(--nav-dark); display: flex;
  }
  .main-nav a {
    color: #fff; text-decoration: none; font-weight: 700; font-size: 16px;
    line-height: 37px; padding: 0 19px; border-right: 1px solid var(--nav-line);
  }
  .main-nav a.is-active { background: var(--active-blue); border-right: 0; }
  .search-field {
    position: absolute; right: 8px; top: 8px; width: 297px; height: 23px;
    background: #fff; border: 1px solid #ccc;
  }
  .search-field svg { position: absolute; right: 3px; top: 1px; }

  .content {
    position: absolute; left: 50px; top: 130px; width: 767px; height: 964px;
    background: var(--panel); border: 1px solid #dedede;
  }
  .banner { position: absolute; left: 19px; top: 19px; width: 730px; height: 230px; background: var(--banner-frame); }
  .banner-panel {
    position: absolute; left: 12px; top: 12px; width: 708px; height: 168px;
    background: var(--banner-green); border: 1px solid #3f8f00; border-radius: 8px; overflow: hidden;
    font-family: "Open Sans", Arial, sans-serif; color: #fff;
  }
  .banner-title { position: absolute; left: 40px; top: 28px; font-size: 58px; line-height: 1; }
  .banner-sub { position: absolute; left: 41px; top: 112px; font-size: 18px; }
  .banner-illustration {
    position: absolute; right: -2px; top: 30px; width: 200px; height: 118px;
    background: linear-gradient(90deg, rgba(255,255,255,0.15), #ffffff 55%);
    border-radius: 60px 0 0 60px;
  }
  .banner-strip { position: absolute; left: 0; bottom: 0; width: 730px; height: 36px; background: var(--banner-strip); }
  .banner-pager { position: absolute; left: 6px; top: 9px; display: flex; gap: 3px; }
  .banner-pager span {
    width: 19px; height: 17px; font-size: 14px; font-weight: 700; text-align: center; line-height: 17px;
    background: #fff; color: #000;
  }
  .banner-pager span.is-current { background: #000; color: #fff; }

  .intro-title { position: absolute; left: 19px; top: 265px; font-size: 26px; color: var(--accent-blue); font-weight: 400; }
  .intro-box {
    position: absolute; left: 19px; top: 316px; width: 730px; height: 402px;
    background: var(--box-grey); padding: 18px 12px; font-size: 15px; line-height: 24px;
  }
  .intro-box p { margin-bottom: 24px; }
  .intro-box h3 { font-size: 18px; font-weight: 400; color: var(--accent-blue); line-height: 26px; }
  .intro-box .more { color: var(--accent-blue); font-weight: 700; text-decoration: none; }

  .news { position: absolute; left: 19px; top: 738px; width: 730px; }
  .news h2 { font-size: 19px; color: var(--heading-grey); line-height: 26px; }
  .news time { display: block; font-size: 15px; line-height: 26px; color: #333; }
  .news h3 { font-size: 19px; color: var(--heading-grey); line-height: 28px; margin-bottom: 18px; }
  .news p { font-size: 15px; line-height: 24px; margin-bottom: 24px; }
  .news .read-more { font-size: 15px; }
  .news hr { border: 0; border-top: 1px solid #dedede; margin-top: 18px; }

  .promo {
    position: absolute; left: 838px; top: 130px; width: 305px; height: 321px;
    background: var(--panel); border: 1px solid #dedede; padding: 22px 18px;
    font-size: 15px; line-height: 24px;
  }
  .promo-kicker { font-size: 14px; font-weight: 700; color: var(--heading-grey); }
  .promo-title { font-size: 19px; font-weight: 700; color: var(--promo-orange); margin: 4px 0 0 10px; line-height: 28px; }
  .promo-lead { margin-top: 14px; width: 130px; }
  .promo-lead .big { font-size: 17px; padding-left: 10px; }
  .promo-illustration {
    position: absolute; right: 22px; top: 78px; width: 130px; height: 92px;
    background: radial-gradient(circle at 60% 50%, #e74c3c, #f39c4a 55%, rgba(255,255,255,0) 75%);
  }
  .promo-text { margin-top: 14px; }
  .promo-actions { margin-top: 16px; display: flex; gap: 4px; }
  .btn {
    font-size: 13px; font-weight: 700; color: #fff; text-decoration: none;
    padding: 0 10px; line-height: 28px; border-radius: 4px;
  }
  .btn-info { background: linear-gradient(#6fd8f7, #27b3e6); }
  .btn-demo { background: linear-gradient(#ff5a4d, var(--btn-red)); }

  .site-footer {
    position: absolute; left: 0; top: 1109px; width: 1200px; height: 56px;
    background: var(--footer); color: #fff; font-size: 13px; padding: 14px 0 0 50px;
  }
</style>
</head>
<body>
  <header class="site-header">
    <div class="brand">Netzhafen</div>
    <nav class="meta-links"><a href="#">Kontakt</a><a href="#">Sitemap</a><a href="#">Impressum</a></nav>
  </header>

  <nav class="main-nav">
    <a href="#" class="is-active">START</a>
    <a href="#">NETZHAFEN</a>
    <a href="#">TIPPS &amp; TOOLS</a>
    <a href="#">KUNDEN</a>
    <a href="#">UNTERNEHMEN</a>
    <div class="search-field">
      <svg width="20" height="20" viewBox="0 0 20 20" aria-hidden="true">
        <circle cx="8" cy="8" r="6" fill="#cfe6f7" stroke="#2a6fa8" stroke-width="2"/>
        <line x1="12.5" y1="12.5" x2="18" y2="18" stroke="#333" stroke-width="3"/>
      </svg>
    </div>
  </nav>

  <main class="content">
    <section class="banner">
      <div class="banner-panel">
        <div class="banner-title">Online-Services</div>
        <div class="banner-sub">Service-Dienstleistungen für Ihr E-Business</div>
        <div class="banner-illustration" role="img" aria-label="Gezeichnete Hand, die auf einen Button tippt"></div>
      </div>
      <div class="banner-strip">
        <div class="banner-pager"><span>1</span><span>2</span><span class="is-current">3</span></div>
      </div>
    </section>

    <h1 class="intro-title">Netzhafen: für Ihr Online-Business!</h1>

    <section class="intro-box">
      <p><strong>Sie möchten im Internet erfolgreich sein und bleiben?</strong> Dann sind wir genau der richtige Partner für Sie. Wir bieten Ihnen eine breite Palette von Dienstleistungen an. Damit können Sie Ihr Unternehmen fit für den harten Konkurrenzkampf im World Wide Web machen.</p>
      <h3>Heben Sie sich von Ihrer Konkurrenz ab</h3>
      <p>Wir bieten Ihnen eine individuelle und professionelle Onlineshop-Erstellung an, mit der Sie ihr E-Business auf ein sicheres Fundament stellen können.<a class="more" href="#">»</a></p>
      <h3>Konzentrieren Sie sich auf das Wesentliche</h3>
      <p>Nutzen Sie unsere umfangreichen Online-Services. Wir erstellen Ihnen z.B. als Dienstleister Inhalte, Artikel und Produktbeschreibungen, die ganz auf Ihren individuellen Bedarf abgestimmt sind.<a class="more" href="#"> »</a></p>
      <h3>Mehr Effizienz für Ihren Onlineshop</h3>
      <p>Optimiertes und auf Ihre Zielgruppe ausgerichtetes Online-Marketing, so dass möglichst viele Kunden Ihr Angebot finden. Mehr Besucher, mehr Umsatz, mehr Gewinn! <a class="more" href="#">»</a></p>
    </section>

    <section class="news">
      <h2>Aktuelle Nachrichten</h2>
      <time>05. Apr 2010 10:45</time>
      <h3>Unternehmensstart Netzhafen</h3>
      <p>Es ist vollbracht: Netzhafen, ein Unternehmen im Bereich E-Commerce &amp; Online-Marketing, geht nach 3 Monaten Gründungsphase an den Start ...</p>
      <a class="read-more" href="#">Weiterlesen …</a>
      <hr>
    </section>
  </main>

  <aside class="promo">
    <div class="promo-kicker">IHR NEUER</div>
    <div class="promo-title">ONLINESHOP 2.0</div>
    <div class="promo-lead">Lassen Sie Ihre<br><span class="big">Konkurenz</span><br>alt aussehen!</div>
    <div class="promo-illustration" role="img" aria-label="Bunte Einkaufstüten mit Prozentzeichen"></div>
    <p class="promo-text">Fordern Sie heute noch Ihren ganz persönlichen Admin Zugang an.</p>
    <div class="promo-actions">
      <a href="#" class="btn btn-info">MEHR INFO</a>
      <a href="#" class="btn btn-demo">DEMO</a>
    </div>
  </aside>

  <footer class="site-footer">© 2010 Netzhafen. Alle Rechte vorbehalten. E-Business Solutions, E-Commerce Service &amp; Online Marketing.</footer>
</body>
</html>
```